IG ad to attract older men for better health #1

I want a bold headline Snapfeed Ad that coordinate with my website design with a racy sexy woman to attract men 45yrs old plus. See Two samples attached

Target Market(s)

Men 45 years old and older

Industry/Entity Type

Health And Wellness

Requirements
Must have
• eye catching appeal to men
Nice to have
• The copy to read
Kestrel61go is the headline at the top of the page. Then the copy reads...
"I want to seduce you to better health with a little T&A. Remove the excuses, provide ridiculously simple tips and advice to get you started on a path of lasting heath." Want more?

```html
<!DOCTYPE html>
<html lang="en">
<head>
<meta charset="utf-8">
<title>Kestrel61go – Snapfeed Ads Carousel</title>
<link href="https://fonts.googleapis.com/css2?family=Inter:wght@400;600;700&family=Rubik:wght@600;700;800&display=swap" rel="stylesheet">
<style>
  :root {
    --board: #52565d;
    --yellow: #ffe600;
    --badge: #f2d22c;
    --white: #ffffff;
    --ink: #111111;
    --screen: #0b0b0b;
    --slide-dark: #141414;
    --logo-grey: #9a9a9a;
    --frame-light: #e4e4e6;
    --frame-dark: #9c9ca2;
    --link: #5b8def;
  }
  * { box-sizing: border-box; margin: 0; padding: 0; }
  html, body { width: 1200px; height: 600px; overflow: hidden; }
  body { background: var(--board); font-family: "Inter", sans-serif; color: var(--white); position: relative; }

  .brand-title { position: absolute; left: 33px; top: 34px; font-family: "Rubik", sans-serif; font-weight: 800; font-size: 46px; line-height: 52px; color: var(--yellow); }
  .board-subtitle { position: absolute; left: 35px; top: 101px; font-size: 21px; font-weight: 700; }

  .slide { position: absolute; top: 226px; width: 157px; height: 157px; overflow: hidden; background: var(--slide-dark); }
  .slide-photo { position: absolute; inset: 0; }
  .slide-logo { position: absolute; top: 10px; font-family: "Rubik", sans-serif; font-weight: 700; font-size: 7.5px; color: var(--logo-grey); }
  .slide-copy { position: absolute; font-family: "Rubik", sans-serif; font-weight: 700; font-size: 14px; line-height: 12.6px; color: var(--white); }
  .slide-copy .hl { display: inline-block; background: var(--yellow); color: var(--ink); padding: 0 2px; font-weight: 800; line-height: 13px; }

  /* phone */
  .phone { position: absolute; left: 23px; top: 165px; width: 177px; height: 359px; border-radius: 30px; background: linear-gradient(135deg, var(--frame-light), var(--frame-dark) 60%, var(--frame-light)); padding: 5px; }
  .phone-screen { position: relative; width: 100%; height: 100%; border-radius: 25px; background: var(--screen); overflow: hidden; border: 3px solid #1c1c1c; }
  .status-bar { position: absolute; left: 0; right: 0; top: 4px; height: 10px; font-size: 5.5px; font-weight: 600; display: flex; justify-content: space-between; padding: 0 14px 0 20px; align-items: center; }
  .notch { position: absolute; left: 50%; top: 0; width: 70px; height: 10px; margin-left: -35px; background: #000; border-radius: 0 0 8px 8px; }
  .app-header { position: absolute; left: 0; right: 0; top: 17px; height: 14px; display: flex; justify-content: space-between; align-items: center; padding: 0 8px; font-size: 7px; font-weight: 600; border-bottom: 0.5px solid #222; }
  .post-head { position: absolute; left: 7px; right: 8px; top: 35px; display: flex; align-items: center; gap: 4px; font-size: 4.5px; line-height: 5.5px; }
  .avatar { width: 11px; height: 11px; border-radius: 50%; background: #3a3a3a; border: 1px solid var(--yellow); }
  .post-head .more { margin-left: auto; font-size: 7px; }
  .phone .slide { top: 49px; left: 0; width: 163px; height: 153px; }
  .feed-cta { position: absolute; left: 0; top: 202px; width: 163px; height: 14px; background: var(--yellow); color: var(--ink); font-size: 5.5px; font-weight: 600; display: flex; align-items: center; justify-content: space-between; padding: 0 8px; }
  .actions { position: absolute; left: 7px; right: 8px; top: 219px; height: 10px; display: flex; align-items: center; }
  .actions .dots { position: absolute; left: 66px; top: 4px; }
  .likes { position: absolute; left: 7px; top: 232px; font-size: 4.5px; font-weight: 600; }
  .caption { position: absolute; left: 7px; right: 8px; top: 241px; font-size: 4.3px; line-height: 5.4px; }
  .caption b { font-weight: 700; }
  .caption .tag { color: var(--link); }
  .nav-bar { position: absolute; left: 0; right: 0; bottom: 8px; height: 14px; display: flex; justify-content: space-around; align-items: center; border-top: 0.5px solid #222; padding-top: 4px; }

  .section-label { position: absolute; width: 200px; text-align: center; font-size: 13px; font-weight: 700; line-height: 16px; }
  .badge { position: absolute; width: 90px; height: 90px; border-radius: 50%; background: var(--badge); color: var(--ink); display: flex; align-items: center; justify-content: center; text-align: center; font-size: 14px; font-weight: 700; line-height: 17px; }
  .brackets { position: absolute; left: 0; top: 0; }
</style>
</head>
<body>
  <div class="brand-title">Kestrel61go</div>
  <div class="board-subtitle">Snapfeed Ads - Carousel</div>

  <!-- feed preview on phone -->
  <div class="phone">
    <div class="phone-screen">
      <div class="notch"></div>
      <div class="status-bar"><span>9:41</span>
        <svg width="16" height="6" viewBox="0 0 16 6" aria-hidden="true"><rect x="0" y="3" width="1.5" height="3" fill="#fff"/><rect x="2.5" y="1.5" width="1.5" height="4.5" fill="#fff"/><rect x="5" y="0" width="1.5" height="6" fill="#fff"/><rect x="9" y="0.5" width="6" height="5" rx="1" fill="none" stroke="#fff" stroke-width="0.7"/><rect x="10" y="1.5" width="4" height="3" fill="#fff"/></svg>
      </div>
      <div class="app-header"><span>Snapfeed</span>
        <svg width="8" height="8" viewBox="0 0 10 10" aria-hidden="true"><path d="M1 1 L9 1 L5 9 L4.5 5 Z" fill="none" stroke="#fff" stroke-width="0.9" stroke-linejoin="round"/></svg>
      </div>
      <div class="post-head"><span class="avatar"></span><span>Kestrel61go<br><span style="opacity:.7">Sponsored</span></span><span class="more">⋮</span></div>

      <div class="slide">
        <div class="slide-photo" role="img" aria-label="Blonde woman in a light blue bikini in a dark gym" style="background:linear-gradient(90deg,#1a1a1a 0%,#262626 50%,#c9a58c 68%,#8fb6c6 82%,#1d1d1d 100%)"></div>
        <div class="slide-logo" style="left:8px">Kestrel61go</div>
        <div class="slide-copy" style="left:8px;top:40px;font-size:13.5px;line-height:12.4px">"I want to<br>seduce you<br>to better<br>health..<br>with a<br>little T&amp;A.</div>
      </div>
      <div class="feed-cta"><span>Join Now</span><span>&gt;</span></div>

      <div class="actions">
        <svg width="40" height="9" viewBox="0 0 40 9" aria-hidden="true" fill="none" stroke="#fff" stroke-width="0.8" stroke-linejoin="round">
          <path d="M4.5 8 L1 4.5 A2 2 0 0 1 4.5 2 A2 2 0 0 1 8 4.5 Z"/>
          <path d="M17 1 A3.5 3.5 0 1 0 19.5 7 L21 8 L20.5 6 A3.5 3.5 0 0 0 17 1 Z"/>
          <path d="M27 1 L34 1 L30.5 8 L30 4.5 Z"/>
        </svg>
        <svg class="dots" width="20" height="2" viewBox="0 0 20 2" aria-hidden="true"><circle cx="1" cy="1" r="0.8" fill="var(--link)"/><circle cx="4.5" cy="1" r="0.7" fill="#888"/><circle cx="8" cy="1" r="0.7" fill="#888"/><circle cx="11.5" cy="1" r="0.7" fill="#888"/><circle cx="15" cy="1" r="0.7" fill="#888"/><circle cx="18.5" cy="1" r="0.7" fill="#888"/></svg>
        <svg style="margin-left:auto" width="7" height="9" viewBox="0 0 7 9" aria-hidden="true"><path d="M1 1 H6 V8 L3.5 6 L1 8 Z" fill="none" stroke="#fff" stroke-width="0.8"/></svg>
      </div>
      <div class="likes">6,173 likes</div>
      <div class="caption"><b>kestrel61go</b><br>Lorem Ipsum is simply dummy text of the printing and typesetting industry. Lorem Ipsum has been the industry's standard dummy text ever since the 1500s, when an unknown printer took a galley of type and scrambled it to make a type specimen book. It has survived not only five centuries, <span class="tag">#Kestrel61go</span></div>

      <div class="nav-bar">
        <svg width="9" height="9" viewBox="0 0 10 10" aria-hidden="true"><path d="M1.5 9 V4.5 L5 1.5 L8.5 4.5 V9 H6 V6.5 H4 V9 Z" fill="none" stroke="#fff" stroke-width="0.9"/></svg>
        <svg width="9" height="9" viewBox="0 0 10 10" aria-hidden="true"><circle cx="4.2" cy="4.2" r="3" fill="none" stroke="#fff" stroke-width="1.3"/><path d="M6.5 6.5 L9 9" stroke="#fff" stroke-width="1.3"/></svg>
        <svg width="9" height="9" viewBox="0 0 10 10" aria-hidden="true"><rect x="1" y="1" width="8" height="8" rx="2" fill="none" stroke="#fff" stroke-width="0.8"/><path d="M5 3 V7 M3 5 H7" stroke="#fff" stroke-width="0.8"/></svg>
        <svg width="9" height="9" viewBox="0 0 10 10" aria-hidden="true"><path d="M5 9 L1.2 5 A2.2 2.2 0 0 1 5 2.4 A2.2 2.2 0 0 1 8.8 5 Z" fill="none" stroke="#fff" stroke-width="0.8"/></svg>
        <svg width="9" height="9" viewBox="0 0 10 10" aria-hidden="true"><circle cx="5" cy="3.3" r="2" fill="none" stroke="#fff" stroke-width="0.8"/><path d="M1.5 9 A3.5 3.5 0 0 1 8.5 9" fill="none" stroke="#fff" stroke-width="0.8"/></svg>
      </div>
    </div>
  </div>

  <!-- carousel slides -->
  <div class="slide" style="left:202px">
    <div class="slide-photo" role="img" aria-label="Blonde woman in a light blue bikini in a dark gym" style="background:linear-gradient(90deg,#1a1a1a 0%,#262626 40%,#c9a58c 60%,#8fb6c6 75%,#2a2a2a 100%)"></div>
    <div class="slide-logo" style="left:7px">Kestrel61go</div>
    <div class="slide-copy" style="left:7px;top:55px">Remove<br>the<br>Excuses,</div>
  </div>

  <div class="slide" style="left:367px">
    <div class="slide-photo" role="img" aria-label="Blonde woman in a light blue bikini in a dark gym" style="background:linear-gradient(90deg,#1a1a1a 0%,#262626 40%,#c9a58c 60%,#8fb6c6 75%,#2a2a2a 100%)"></div>
    <div class="slide-logo" style="left:7px">Kestrel61go</div>
    <div class="slide-copy" style="left:7px;top:55px">Provide<br>Ridiculously<br>Simple Tips</div>
  </div>

  <div class="slide" style="left:530px">
    <div class="slide-photo" role="img" aria-label="Dark-haired woman in a black bikini in a dark gym" style="background:linear-gradient(90deg,#1a1a1a 0%,#a47a5e 25%,#1c1c1c 45%,#2a2a2a 100%)"></div>
    <div class="slide-logo" style="right:7px">Kestrel61go</div>
    <div class="slide-copy" style="right:7px;top:55px;text-align:right">and Advice<br>to Get You<br><span class="hl">STARTED</span></div>
  </div>

  <div class="slide" style="left:695px">
    <div class="slide-photo" role="img" aria-label="Dark-haired woman in a black bikini in a dark gym" style="background:linear-gradient(90deg,#1a1a1a 0%,#a47a5e 25%,#1c1c1c 45%,#2a2a2a 100%)"></div>
    <div class="slide-logo" style="right:7px">Kestrel61go</div>
    <div class="slide-copy" style="right:7px;top:55px;text-align:right">On a Path<br>of Lasting<br><span class="hl">HEALTH</span></div>
  </div>

  <div class="slide" style="left:859px">
    <div class="slide-photo" role="img" aria-label="Athletic woman in black sportswear in a dark gym" style="background:linear-gradient(90deg,#1a1a1a 0%,#2a2a2a 30%,#a47a5e 50%,#2a2a2a 70%,#1a1a1a 100%)"></div>
    <div class="slide-logo" style="right:7px">Kestrel61go</div>
    <div class="slide-copy" style="left:39px;top:64px;font-size:22px;line-height:19px;font-weight:800">WANT<br><span class="hl" style="margin-left:-3px;line-height:19px">MORE?</span></div>
  </div>

  <div class="slide" style="left:1023px">
    <div class="slide-photo" role="img" aria-label="Dark gym interior" style="background:linear-gradient(180deg,#1a1a1a 0%,#2b2b2b 60%,#161616 100%)"></div>
    <div style="position:absolute;left:0;right:0;top:50px;text-align:center">
      <div style="font-size:8.5px;font-weight:700">Join Now!</div>
      <div style="font-family:'Rubik',sans-serif;font-weight:800;font-size:17px;color:var(--yellow);margin-top:3px">Kestrel61go</div>
      <div style="font-size:5px;font-weight:600;margin-top:1px">Out of shape and overweight</div>
    </div>
  </div>

  <!-- section brackets -->
  <svg class="brackets" width="1200" height="600" aria-hidden="true">
    <g fill="none" stroke="#ffffff" stroke-width="1.5">
      <polyline points="601,208 601,180 788,180 788,210"/>
      <polyline points="267,396 267,425 454,425 454,394"/>
    </g>
    <g fill="#ffffff">
      <circle cx="601" cy="208" r="3"/><circle cx="788" cy="210" r="3"/>
      <circle cx="267" cy="396" r="3"/><circle cx="454" cy="394" r="3"/>
    </g>
  </svg>

  <div class="section-label" style="left:595px;top:133px">Slide 4-5<br>Promising Part</div>
  <div class="section-label" style="left:259px;top:437px">Slide 1-3<br>Seducing Part</div>

  <div class="badge" style="left:892px;top:397px">Triggering</div>
  <div class="badge" style="left:1056px;top:397px">Call to<br>Action</div>
</body>
</html>
```